Marrowby Electric
Business Cards
Marrowby Electric -
Creative Brief
Modern
Peter Marrowby
Owner
17 Orvell St. Brookfield CT. 06804
pete@marrowbyelectric-example.com
www.marrowbyelectric-example.com
E-1 #374620

```html
<!DOCTYPE html>
<html lang="en">
<head>
<meta charset="utf-8">
<title>Marrowby Electric – Business Cards</title>
<link rel="stylesheet" href="https://fonts.googleapis.com/css2?family=Montserrat:wght@400;600;800&display=swap">
<style>
  :root {
    --stage: #e9e6e1;
    --navy-deep: #062247;
    --navy: #0c3d78;
    --blue: #1f6fb5;
    --blue-light: #4fa3e0;
    --ink: #1b1b1b;
    --card-white: #ffffff;
    --text-light: #ffffff;
    --text-dark: #222a33;
  }
  * { box-sizing: border-box; margin: 0; padding: 0; }
  html, body { width: 1200px; height: 646px; overflow: hidden; }
  body {
    background: var(--stage);
    font-family: "Montserrat", sans-serif;
    position: relative;
  }
  .card {
    position: absolute;
    top: 173px;
    width: 525px;
    height: 300px;
    border-radius: 4px;
    overflow: hidden;
    box-shadow: 0 10px 28px rgba(0,0,0,0.18);
  }
  .card--front {
    left: 50px;
    background: radial-gradient(ellipse at 50% 38%, var(--blue-light) 0%, var(--blue) 28%, var(--navy) 60%, var(--navy-deep) 100%);
  }
  .card--back {
    left: 625px;
    background: var(--card-white);
  }
  .brand {
    position: absolute;
    display: flex;
    flex-direction: column;
    align-items: center;
    gap: 14px;
  }
  .card--front .brand { left: 0; right: 0; top: 92px; }
  .card--back .brand { left: 20px; width: 190px; top: 100px; }
  .brand__mark {
    width: 50px;
    height: 50px;
    border-radius: 8px;
    background: var(--blue-light);
  }
  .card--back .brand__mark { background: var(--blue); }
  .brand__name {
    font-weight: 800;
    font-size: 22px;
    letter-spacing: 1px;
    line-height: 1.1;
    text-align: center;
    text-transform: uppercase;
  }
  .card--front .brand__name { color: var(--text-light); }
  .card--back .brand__name { color: var(--text-dark); }
  .back-swoosh {
    position: absolute;
    inset: 0;
  }
  .contact {
    position: absolute;
    right: 22px;
    top: 40px;
    text-align: right;
    color: var(--text-light);
    font-size: 9.5px;
    line-height: 1.6;
  }
  .contact__name { font-weight: 600; font-size: 13px; }
  .contact__role { font-size: 9px; margin-bottom: 12px; }
  .contact__line { display: flex; justify-content: flex-end; align-items: center; gap: 6px; white-space: nowrap; }
  .contact__gap { margin-top: 10px; }
  .icon { width: 9px; height: 9px; fill: var(--text-light); flex: none; }
</style>
</head>
<body>
  <section class="card card--front" aria-label="Card front">
    <div class="brand">
      <span class="brand__mark"></span>
      <span class="brand__name">Marrowby<br>Electric</span>
    </div>
  </section>

  <section class="card card--back" aria-label="Card back">
    <svg class="back-swoosh" viewBox="0 0 525 300" width="525" height="300" aria-hidden="true">
      <defs>
        <linearGradient id="panelBlue" x1="0" y1="0" x2="1" y2="1">
          <stop offset="0" stop-color="#2f86cc"/>
          <stop offset="1" stop-color="#0c3d78"/>
        </linearGradient>
      </defs>
      <path d="M244 0 C204 60 200 110 234 150 C272 190 264 250 227 300 L525 300 L525 0 Z" fill="#1b1b1b"/>
      <path d="M262 0 C222 60 218 110 252 150 C290 190 282 250 245 300 L525 300 L525 0 Z" fill="url(#panelBlue)"/>
    </svg>
    <div class="brand">
      <span class="brand__mark"></span>
      <span class="brand__name">Marrowby<br>Electric</span>
    </div>
    <div class="contact">
      <div class="contact__name">Peter Marrowby</div>
      <div class="contact__role">Owner</div>
      <div class="contact__line">17 Orvell St.</div>
      <div class="contact__line">Brookfield CT. 06804
        <svg class="icon" viewBox="0 0 10 10"><path d="M5 0a3.5 3.5 0 0 0-3.5 3.5C1.5 6 5 10 5 10s3.5-4 3.5-6.5A3.5 3.5 0 0 0 5 0z"/></svg>
      </div>
      <div class="contact__line contact__gap">203-555-0142
        <svg class="icon" viewBox="0 0 10 10"><path d="M2 0l2 2.5-1 1.2a6 6 0 0 0 3.3 3.3l1.2-1L10 8l-1.5 2C4 10 0 6 0 1.5z"/></svg>
      </div>
      <div class="contact__line">203-555-0178
        <svg class="icon" viewBox="0 0 10 10"><rect x="2.5" y="0" width="5" height="10" rx="1"/></svg>
      </div>
      <div class="contact__line">pete1968wv
        <svg class="icon" viewBox="0 0 10 10"><circle cx="5" cy="5" r="5"/></svg>
      </div>
      <div class="contact__line contact__gap">pete@marrowbyelectric-example.com</div>
      <div class="contact__line">www.marrowbyelectric-example.com</div>
      <div class="contact__line contact__gap">License: E-1 #374620</div>
    </div>
  </section>
</body>
</html>
```